Chiropractic Auto Accident Billboard

Billboard for Auto Accident Chiropractor
Kestrelwood Rehab
(770) 48-SPINE
Habla Espanol
Same Day Appointments - Locations across Georgia
INJURED IN A CAR ACCIDENT?

Target Market(s)

People in Auto Accidents

Industry/Entity Type

Personal Injury

Requirements
Must have
• BIG PHONE Number

```html
<!DOCTYPE html>
<html lang="en">
<head>
<meta charset="utf-8">
<title>Kestrelwood Rehab – Auto Accident Chiropractor Billboard</title>
<link rel="stylesheet" href="https://fonts.googleapis.com/css2?family=Bebas+Neue&family=Poppins:wght@600;700;800&display=swap">
<style>
  :root {
    --page-bg: #e2e2e2;
    --ink-black: #050505;
    --ink-dark: #141414;
    --white: #ffffff;
    --orange: #f26a1b;
    --orange-light: #f7923a;
    --green-dark: #1d6a2b;
    --green-bright: #5fb83c;
    --green-tick: #4caf3c;
    --curve-dark: #2f2f2f;
  }
  * { margin: 0; padding: 0; box-sizing: border-box; }
  html, body { width: 1067px; height: 1200px; overflow: hidden; }
  body { background: var(--page-bg); position: relative; font-family: "Poppins", sans-serif; }

  .billboard {
    position: absolute; left: 33px; top: 442px;
    width: 1000px; height: 316px; overflow: hidden;
    background: var(--white);
    box-shadow: 0 6px 14px rgba(0,0,0,0.18);
  }
  .band-top { position: absolute; left: 0; top: 0; width: 100%; height: 137px; background: var(--ink-black); }
  .band-green {
    position: absolute; left: 0; top: 137px; width: 100%; height: 66px;
    background: linear-gradient(90deg, var(--green-dark) 0%, #2f8a31 35%, var(--green-bright) 68%, var(--green-dark) 88%);
  }
  .band-white { position: absolute; left: 0; top: 203px; width: 100%; height: 113px; background: var(--white); }

  .portrait-art { position: absolute; left: 0; top: 0; width: 1000px; height: 316px; }

  .brand { position: absolute; left: 28px; top: 44px; display: flex; align-items: center; gap: 10px; }
  .brand-dot { width: 40px; height: 40px; border-radius: 50%; background: var(--green-bright); flex: none; }
  .brand-name { font-weight: 700; font-size: 20px; line-height: 1.1; color: var(--green-bright); width: 150px; }

  .headline {
    position: absolute; left: 258px; top: 42px;
    font-family: "Bebas Neue", sans-serif; font-size: 50px; line-height: 1;
    color: var(--white); letter-spacing: 0.2px; white-space: nowrap;
  }
  .headline .accent { color: var(--orange); }

  .perks { position: absolute; left: 262px; top: 96px; display: flex; gap: 12px; white-space: nowrap; }
  .perk { display: flex; align-items: center; gap: 4px; font-weight: 600; font-size: 15.5px; color: var(--white); }
  .perk svg { width: 12px; height: 12px; }

  .question {
    position: absolute; left: 36px; top: 144px;
    font-weight: 800; font-size: 41px; line-height: 52px;
    color: var(--white); white-space: nowrap; letter-spacing: -0.3px;
  }

  .call { position: absolute; left: 34px; top: 214px; display: flex; align-items: center; white-space: nowrap; }
  .call-icon { width: 60px; height: 60px; margin-right: 10px; }
  .phone { font-weight: 700; font-size: 64px; line-height: 90px; color: var(--ink-dark); letter-spacing: -1px; }
  .divider { width: 2px; height: 44px; background: var(--ink-dark); margin: 0 16px 0 20px; }
  .spanish { font-weight: 600; font-size: 25px; line-height: 1.05; color: var(--ink-dark); }
</style>
</head>
<body>
  <section class="billboard" aria-label="Auto accident chiropractor billboard">
    <div class="band-top"></div>
    <div class="band-green"></div>
    <div class="band-white"></div>

    <svg class="portrait-art" viewBox="0 0 1600 505" preserveAspectRatio="none">
      <defs>
        <radialGradient id="portraitTone" cx="0.6" cy="0.4" r="0.7">
          <stop offset="0" stop-color="#f7923a"/>
          <stop offset="0.55" stop-color="#f26a1b"/>
          <stop offset="1" stop-color="#e25a12"/>
        </radialGradient>
      </defs>
      <path role="img" aria-label="Portrait of the smiling chiropractor in a dark blazer and light blue shirt, set on an orange leaf-patterned background"
            d="M1262 0 C1327 80 1337 180 1287 300 C1252 390 1257 450 1297 505 L1600 505 L1600 0 Z"
            fill="url(#portraitTone)"/>
      <path d="M1200 0 L1256 0 C1321 80 1331 180 1281 300 C1246 390 1251 450 1291 505 L1242 505 C1197 450 1202 380 1240 300 C1284 200 1272 90 1200 0 Z"
            fill="var(--curve-dark)"/>
      <path d="M1259 0 C1324 80 1334 180 1284 300 C1249 390 1254 450 1294 505"
            fill="none" stroke="var(--white)" stroke-width="4"/>
    </svg>

    <div class="brand">
      <span class="brand-dot"></span>
      <span class="brand-name">Kestrelwood Rehab</span>
    </div>

    <h1 class="headline">AUTO ACCIDENT <span class="accent">CHIROPRACTOR</span></h1>

    <ul class="perks">
      <li class="perk">
        <svg viewBox="0 0 12 12" aria-hidden="true"><circle cx="6" cy="6" r="6" fill="var(--green-tick)"/><path d="M3.2 6.2 L5.2 8 L8.8 4.2" fill="none" stroke="#fff" stroke-width="1.6" stroke-linecap="round" stroke-linejoin="round"/></svg>
        Same Day Appointments
      </li>
      <li class="perk">
        <svg viewBox="0 0 12 12" aria-hidden="true"><circle cx="6" cy="6" r="6" fill="var(--green-tick)"/><path d="M3.2 6.2 L5.2 8 L8.8 4.2" fill="none" stroke="#fff" stroke-width="1.6" stroke-linecap="round" stroke-linejoin="round"/></svg>
        Locations across Georgia
      </li>
    </ul>

    <h2 class="question">INJURED IN A CAR ACCIDENT?</h2>

    <div class="call">
      <svg class="call-icon" viewBox="0 0 60 60" aria-hidden="true">
        <path d="M8 8 C4 12 4 20 10 30 C16 40 26 50 36 54 C44 57 50 55 53 50 L46 41 C44 39 41 39 39 41 L35 44 C29 41 21 33 17 26 L21 22 C23 20 23 17 21 15 L13 7 C11 5 9.5 6.5 8 8 Z" fill="var(--orange)"/>
        <path d="M32 14 A10 10 0 0 1 42 24" fill="none" stroke="var(--orange)" stroke-width="2.6" stroke-linecap="round"/>
        <path d="M33 7 A17 17 0 0 1 49 23" fill="none" stroke="var(--orange)" stroke-width="2.6" stroke-linecap="round"/>
        <path d="M31 21 A4 4 0 0 1 35 25" fill="none" stroke="var(--orange)" stroke-width="2.6" stroke-linecap="round"/>
      </svg>
      <span class="phone">(770) 48-SPINE</span>
      <span class="divider"></span>
      <span class="spanish">Habla<br>Espanol</span>
    </div>
  </section>
</body>
</html>
```